Zero Tax Seminar Postcard Design

I need a postcard designed that is 5.5" x 8.5". Color front and back with space for an address block and postal indicia. I will provide the bullet points and copy. I need assistance with the layout, organization and perhaps a couple of images, etc. This postcard will drive individuals to a web site to register for a 90-minute seminar teaching them how to minimize or eliminate their income taxes during retirement.
Target Market(s)
Married Couples, ages 50 - 70. Successful and affluent. People that appreciate and value professional advice and relationships.
Requirements
Must have
- Bright and Bold.  Compelling and attention grabbing.
Call to action #1 - Go to website immediately for further information.
Call to action #2 - Call the office immediately to register.

```html
<!DOCTYPE html>
<html lang="en">
<head>
<meta charset="utf-8">
<title>Tax Freedom Blueprint Seminar Postcard</title>
<link href="https://fonts.googleapis.com/css2?family=Cinzel:wght@400;700&family=Crimson+Text:wght@400;700&family=Fjalla+One&family=Oswald:wght@500&family=Arimo&display=swap" rel="stylesheet">
<style>
  :root{
    --backdrop:#6e4a2c;
    --charcoal:#2b2b2b;
    --gold:#e0a91f;
    --white:#ffffff;
    --ink:#222222;
    --photo-a:#7d97b3;
    --photo-b:#b7c6d3;
    --photo-back:#5b8fc9;
  }
  *{box-sizing:border-box;margin:0;padding:0}
  html,body{width:782px;height:1200px;overflow:hidden;background:var(--backdrop)}
  .canvas{position:relative;width:782px;height:1200px}
  .card{position:absolute;left:40px;width:700px;height:542px;background:var(--white);overflow:hidden}
  .card--front{top:40px}
  .card--back{top:620px}
  .card svg.art{position:absolute;inset:0}

  .front-questions{position:absolute;left:22px;top:50px;width:392px;list-style:none;
    font-family:"Arimo",Arial,sans-serif;font-size:13.2px;line-height:19px;color:var(--white)}
  .front-questions li{position:relative;padding-left:14px;margin-bottom:18px}
  .front-questions li::before{content:"";position:absolute;left:0;top:6px;width:8px;height:8px;border-radius:50%;background:var(--gold)}
  .front-headline{position:absolute;left:22px;top:274px;width:400px;font-family:"Cinzel",serif;font-weight:400;line-height:21px}
  .front-headline .lead{display:block;font-size:26px;line-height:34px;color:var(--gold)}
  .front-headline .gold{display:block;font-size:15.5px;color:var(--gold);white-space:nowrap}
  .front-headline .plain{display:block;font-size:15px;color:var(--white);white-space:nowrap}
  .brand-mark{position:absolute;right:24px;bottom:40px;font-family:"Cinzel",serif;font-size:24px;color:var(--gold);display:flex;align-items:center;gap:8px}
  .brand-mark .dot{width:12px;height:12px;border-radius:50%;background:var(--gold)}

  .back-intro{position:absolute;left:0;top:36px;width:470px;font-family:"Crimson Text",serif;
    font-size:17.5px;line-height:21.2px;color:var(--white)}
  .back-intro span{display:block;white-space:nowrap}
  .back-intro strong{font-weight:700}
  .program-name{position:absolute;left:158px;top:184px;font-family:"Crimson Text",serif;font-weight:700;font-size:21px;color:var(--white)}
  .back-prompt{position:absolute;left:25px;top:236px;font-family:"Fjalla One",sans-serif;
    font-size:15px;line-height:22.5px;color:var(--gold);white-space:nowrap}
  .back-prompt .first{padding-left:63px}
  .cta{position:absolute;border-radius:50%;display:flex;align-items:center;justify-content:center;text-align:center;
    font-family:"Oswald",sans-serif;font-weight:500;color:var(--ink);text-transform:uppercase}
  .cta--web{left:50px;top:315px;width:142px;height:142px;font-size:17px;line-height:18.5px;
    background:radial-gradient(circle,#f2c449 0 66%,#a77710 67% 69%,#f4f4f4 70% 80%,#8c8c8c 88%,#444 100%)}
  .cta--call{left:217px;top:328px;width:120px;height:120px;font-size:14.5px;line-height:16px;
    background:radial-gradient(circle,#f1f1f1 0 66%,#9a9a9a 67% 69%,var(--gold) 70% 84%,#8a6210 100%)}
  .company-name{position:absolute;left:0;top:466px;width:240px;text-align:center;font-family:"Cinzel",serif;
    font-size:21px;line-height:25px;color:var(--gold)}
  .stamp-box{position:absolute;left:604px;top:100px;width:58px;height:56px;border:1.5px solid var(--ink)}
  .address-line{position:absolute;left:497px;width:168px;height:1px;background:var(--ink)}
</style>
</head>
<body>
<div class="canvas">

  <section class="card card--front">
    <svg class="art" width="700" height="542" viewBox="0 0 700 542">
      <defs>
        <linearGradient id="frontPhoto" x1="0" y1="0" x2="1" y2="1">
          <stop offset="0" stop-color="var(--photo-a)"/>
          <stop offset="1" stop-color="var(--photo-b)"/>
        </linearGradient>
      </defs>
      <rect width="700" height="542" fill="url(#frontPhoto)" role="img" aria-label="Photo of a man with raised arms in a green field under a sunrise sky"/>
      <path d="M0,0 H330 C430,90 450,330 290,440 C220,480 90,480 0,460 Z" fill="var(--charcoal)" stroke="var(--gold)" stroke-width="5"/>
      <path d="M0,500 C260,540 560,430 700,230 V542 H0 Z" fill="var(--gold)"/>
      <path d="M0,508 C270,545 570,440 700,248 V542 H0 Z" fill="var(--charcoal)"/>
      <path d="M0,520 C280,548 580,450 700,262 V542 H0 Z" fill="var(--white)"/>
    </svg>
    <ul class="front-questions">
      <li>Are you upset or even angry at the Federal and State government for confiscating more and more of your hard earned money??</li>
      <li>Do you realize that many financial experts agree that income taxes need to double in the next ten years or else we will fly head over heels into the next looming financial disaster??</li>
      <li>How would you like to dramatically decrease or even eliminate your income taxes during your retirement years?? (It is possible!!)</li>
    </ul>
    <h1 class="front-headline">
      <span class="lead">A Unique, One-Of-A-Kind</span>
      <span class="gold">Program Reveals Little Known Secrets</span>
      <span class="plain">Used By America’s Wealthiest Families To</span>
      <span class="plain">Reduce And Even Eliminate Their Income</span>
      <span class="plain">Taxes During Their Retirement Years</span>
    </h1>
    <div class="brand-mark"><span class="dot"></span>Hale Wealth</div>
  </section>

  <section class="card card--back">
    <svg class="art" width="700" height="542" viewBox="0 0 700 542">
      <path d="M0,0 H470 C525,150 490,420 170,542 H0 Z" fill="var(--gold)"/>
      <path d="M0,0 H458 C510,150 475,410 155,542 H0 Z" fill="var(--charcoal)"/>
      <path d="M0,0 H196 C222,90 190,210 0,235 Z" fill="var(--photo-back)" stroke="var(--gold)" stroke-width="5" role="img" aria-label="Photo of colourful hot air balloons against a blue sky"/>
    </svg>
    <p class="back-intro">
      <span style="padding-left:212px">If you would like to move forward</span>
      <span style="padding-left:212px">but seem to be a little stuck, then a</span>
      <span style="padding-left:203px">special <strong>90-MINUTE SEMINAR</strong></span>
      <span style="padding-left:212px">will help you discover how to</span>
      <span style="padding-left:198px">dramatically reduce or even eliminate</span>
      <span style="padding-left:189px">income taxes during your retirement</span>
      <span style="padding-left:176px">years. This seminar is called the</span>
    </p>
    <h2 class="program-name">Tax Freedom Blueprint</h2>
    <p class="back-prompt"><span class="first">Well, what are you waiting for?? Just review the</span><br>dates and times listed to the right of this letter and<br>register for our next Tax Freedom Blueprint Seminar</p>
    <div class="cta cta--web">Go to website<br>immediately<br>for further<br>information</div>
    <div class="cta cta--call">Call the<br>office<br>immediately<br>to register</div>
    <p class="company-name">Marcus Hale<br>Wealth Group</p>
    <div class="stamp-box"></div>
    <div class="address-line" style="top:318px"></div>
    <div class="address-line" style="top:345px"></div>
    <div class="address-line" style="top:372px"></div>
  </section>

</div>
</body>
</html>
```